Bright Harbor Workshops business card design

Needing a business card design using an existing logo. Double sided card and we will be printing using rounded corners. Can also use metallics if appropriate. The design needs to be professional and modern.

Target Market(s)

Professional organisations

Industry/Entity Type

Business

Contact Information for Business Card

busines name, person name, email, website, phone, address,

Colors

Designer to choose colors to be used in the design.

Requirements
Must have
• Use existing 'Bright Harbor Workshops' logo Using uploaded logo design. Simple and modern design. Black,white,silver,greys as the dominant colouring. Can introduce another single colour. Must also include a small version of the attached 'KDL' logo on the card (white and black versions uploaded also)
Nice to have
• Something modern
Should not have
• Additional images

```html
<!DOCTYPE html>
<html lang="en">
<head>
<meta charset="utf-8">
<title>Bright Harbor Workshops – Business Card</title>
<link href="https://fonts.googleapis.com/css2?family=Montserrat:wght@400;500;600&display=swap" rel="stylesheet">
<style>
  :root {
    --stage: #e3e4e6;
    --card-black: #0b0b0c;
    --card-sheen: #2a2a2c;
    --white: #ffffff;
    --soft-white: #e9e9ea;
    --silver: #b9bcc0;
    --rule: #8d8f93;
  }
  * { margin: 0; padding: 0; box-sizing: border-box; }
  html, body { width: 1200px; height: 800px; overflow: hidden; }
  body {
    background: var(--stage);
    font-family: "Montserrat", sans-serif;
    color: var(--white);
    position: relative;
  }
  .card {
    position: absolute;
    top: 250px;
    width: 520px;
    height: 300px;
    border-radius: 26px;
    background: linear-gradient(115deg, var(--card-black) 0%, var(--card-sheen) 38%, var(--card-black) 62%, #151516 100%);
    border: 2px solid var(--silver);
    overflow: hidden;
  }
  .card--front { left: 50px; }
  .card--back { left: 630px; }

  /* Front */
  .brand {
    position: absolute;
    left: 92px;
    top: 100px;
    display: flex;
    align-items: center;
    gap: 14px;
  }
  .brand__mark {
    width: 48px; height: 48px;
    border: 2px solid var(--white);
    border-radius: 50%;
  }
  .brand__name {
    font-size: 17px;
    font-weight: 500;
    line-height: 1.15;
    letter-spacing: 1.5px;
    text-transform: uppercase;
    color: var(--white);
  }
  .brand__tagline {
    position: absolute;
    left: 154px;
    top: 150px;
    font-size: 7.5px;
    font-weight: 500;
    color: var(--soft-white);
    letter-spacing: 0.3px;
  }
  .membership {
    position: absolute;
    right: 30px;
    bottom: 60px;
    display: flex;
    align-items: center;
    gap: 8px;
  }
  .membership__mark {
    width: 14px; height: 14px;
    background: var(--white);
    border-radius: 50%;
  }
  .membership__name {
    font-size: 16px;
    font-weight: 500;
    color: var(--white);
  }
  .membership__divider {
    width: 1px; height: 38px;
    background: var(--soft-white);
    margin: 0 2px;
  }
  .membership__text {
    font-size: 7px;
    line-height: 1.3;
    color: var(--soft-white);
  }

  /* Back */
  .business-name {
    position: absolute;
    right: 34px;
    top: 42px;
    font-size: 38px;
    font-weight: 600;
    letter-spacing: 1px;
    white-space: nowrap;
  }
  .rule {
    position: absolute;
    height: 1px;
    background: var(--rule);
  }
  .rule--top { left: 150px; right: 34px; top: 112px; }
  .rule--bottom { left: 30px; right: 34px; top: 208px; }
  .person {
    position: absolute;
    left: 30px;
    top: 148px;
  }
  .person__name { font-size: 18px; font-weight: 500; line-height: 1.2; }
  .person__role { font-size: 13px; color: var(--soft-white); }
  .contact {
    position: absolute;
    display: flex;
    align-items: center;
    gap: 7px;
    font-size: 12.5px;
    color: var(--soft-white);
  }
  .contact svg { width: 13px; height: 13px; fill: var(--soft-white); flex: none; }
  .contact--email { left: 200px; top: 168px; }
  .contact--web { left: 360px; top: 140px; }
  .contact--phone { left: 30px; top: 228px; }
  .address {
    position: absolute;
    left: 260px;
    top: 226px;
    font-size: 13.5px;
    color: var(--white);
  }
</style>
</head>
<body>

<section class="card card--front" aria-label="Card front">
  <div class="brand">
    <span class="brand__mark"></span>
    <span class="brand__name">Bright Harbor<br>Workshops</span>
  </div>
  <p class="brand__tagline">Evidence-Based Training &amp; Development</p>

  <div class="membership">
    <span class="membership__mark"></span>
    <span class="membership__name">KDL</span>
    <span class="membership__divider"></span>
    <span class="membership__text">Member<br>Kestrel<br>Design<br>League Ltd</span>
  </div>
</section>

<section class="card card--back" aria-label="Card back">
  <h1 class="business-name">BUSINES NAME</h1>
  <div class="rule rule--top"></div>

  <div class="person">
    <p class="person__name">Your Name</p>
    <p class="person__role">Position</p>
  </div>

  <p class="contact contact--email">
    <svg viewBox="0 0 16 16" aria-hidden="true"><path d="M1 3h14v10H1z M2 4.2v.4l6 4 6-4v-.4z" fill-rule="evenodd"/></svg>
    name@email.com
  </p>
  <p class="contact contact--web">
    <svg viewBox="0 0 16 16" aria-hidden="true"><path fill-rule="evenodd" d="M8 1a7 7 0 1 1 0 14A7 7 0 0 1 8 1zm-1 1.6C5.6 3.5 5 5.6 5 7h2zM9 2.6V7h2c0-1.4-.6-3.5-2-4.4zM2.6 7H4c0-1.5.4-2.9 1-3.9A5.6 5.6 0 0 0 2.6 7zm8.4-3.9c.6 1 1 2.4 1 3.9h1.4A5.6 5.6 0 0 0 11 3.1zM2.6 9A5.6 5.6 0 0 0 5 12.9C4.4 11.9 4 10.5 4 9zM5 9c0 1.4.6 3.5 2 4.4V9zm4 0v4.4c1.4-.9 2-3 2-4.4zm3 0c0 1.5-.4 2.9-1 3.9A5.6 5.6 0 0 0 13.4 9z"/></svg>
    www.website.com
  </p>

  <div class="rule rule--bottom"></div>

  <p class="contact contact--phone">
    <svg viewBox="0 0 16 16" aria-hidden="true"><path d="M3.6 1.5l2.3 2.6-1.3 1.6c.9 1.9 2.1 3.2 4 4.1l1.6-1.3 2.6 2.3-1.2 2.2C6.7 12.8 3.2 9.3 1.4 2.7z"/></svg>
    000.000.0000
  </p>
  <p class="address">Address here</p>
</section>

</body>
</html>
```